KESTRA FLOW SUPPLY business card

We need a new business card for our company "Kestra Flow Supply". The company is very simple, we supply bulk heated water to the oilfield and industry. I have included a few images of cards that I like so that you have an idea of the direction I want to go. I will leave fonts up to the designer. I have also included our logo.
Updates

Hello Designers,  if there are any more submissions coming in you might consider using other background colors than black.  I am looking for a little bit of variety before making the decision.

Thanks,

Dale

Sorry, I meant to say background colors other than just black and white.

Thanks,

Dale

Target Market(s)

Ages 20 to 60. Oilfield consultants and Oil and Gas Companies

Industry/Entity Type

Business

Font styles to use
Sans Serif

Requirements
Must have
• Dale Fenwick

email info@kestraflowsupply.example

Phone # 555-318-2047
Fax 555-376-9150

Site 713, Box 2, Comp 4, RR3
Alder Falls, WR, X9Z 4Q8

3-17-52-4 W4M
Hwy 905 Between RR37 & RR38

**Must have our logo

Nice to have
• Would be nice to have " Bulk Heated Water" somewhere on the card

The logo with the flame large across the background might look ok? The name of the company is KESTRA FLOW SUPPLY, but it probably isn't necessary to have the hot water under the logo all the time if you decide it looks better. As long as it is included somewhere on the card. The style of the KESTRA can change slightly (ie:; can be slanted).

The colors of the logo can change, but it might be nice to have the original color and logo somewhere small (corner?)

```html
<!DOCTYPE html>
<html lang="en">
<head>
<meta charset="utf-8">
<title>Kestra Flow Supply – Business Card</title>
<link rel="stylesheet" href="https://fonts.googleapis.com/css2?family=Arimo:wght@400;700&display=swap">
<style>
  :root {
    --backdrop: #d9d9d9;
    --card-black: #050505;
    --card-front-black: #0b0b0c;
    --brand-blue: #5bb8dc;
    --band-blue: #1a86c0;
    --text-white: #ffffff;
  }
  * { box-sizing: border-box; margin: 0; padding: 0; }
  html, body {
    width: 1200px; height: 1000px; overflow: hidden;
    background: var(--backdrop);
    font-family: "Arimo", Arial, sans-serif;
  }
  .canvas { position: relative; width: 1200px; height: 1000px; }

  .card {
    position: absolute; width: 630px; height: 360px;
    overflow: hidden; box-shadow: 0 6px 18px rgba(0,0,0,.25);
  }

  /* Front */
  .card-front { left: 490px; top: 90px; background: var(--card-front-black); }
  .front-mark {
    position: absolute; left: 70px; top: 60px; width: 240px; height: 240px;
    border-radius: 50%;
    background: radial-gradient(circle at 40% 40%, var(--brand-blue), var(--band-blue));
  }
  .front-name {
    position: absolute; left: 340px; top: 130px; width: 260px;
    color: var(--brand-blue); font-weight: 700; font-size: 38px; line-height: 1.05;
  }

  /* Back */
  .card-back { left: 80px; top: 540px; background: var(--card-black); }
  .back-mark {
    position: absolute; left: 40px; top: 40px; width: 210px; height: 210px;
    border-radius: 50%;
    background: radial-gradient(circle at 40% 40%, var(--brand-blue), var(--band-blue));
  }
  .back-brand {
    position: absolute; left: 40px; top: 262px; width: 260px;
    color: var(--brand-blue); font-weight: 700; font-size: 20px;
  }
  .back-band {
    position: absolute; left: 0; right: 0; bottom: 0; height: 26px;
    background: var(--band-blue);
  }
  .divider {
    position: absolute; left: 330px; top: 95px; width: 2px; height: 150px;
    background: linear-gradient(var(--band-blue), rgba(26,134,192,0));
  }
  .contact {
    position: absolute; left: 350px; top: 88px; color: var(--text-white);
    font-size: 13px; line-height: 1.35;
  }
  .contact-name { font-size: 19px; margin: 0 0 10px 38px; }
  .contact-row { display: flex; align-items: flex-start; gap: 10px; margin-bottom: 4px; }
  .contact-row svg { width: 14px; height: 14px; flex: none; margin-top: 2px; fill: var(--text-white); }
  .address { line-height: 1.3; }
</style>
</head>
<body>
<main class="canvas">

  <section class="card card-front" aria-label="Card front">
    <div class="front-mark" aria-hidden="true"></div>
    <div class="front-name">KESTRA FLOW SUPPLY</div>
  </section>

  <section class="card card-back" aria-label="Card back">
    <div class="back-mark" aria-hidden="true"></div>
    <div class="back-brand">KESTRA FLOW SUPPLY</div>
    <div class="divider"></div>

    <div class="contact">
      <div class="contact-name">Dale Fenwick</div>

      <div class="contact-row">
        <svg viewBox="0 0 16 16" aria-label="Phone"><path d="M2 5c0-2 3-3 6-3s6 1 6 3v1h-3V5H5v1H2zM4 7h8l2 6H2z"/></svg>
        <span>555 318 2047</span>
      </div>
      <div class="contact-row">
        <svg viewBox="0 0 16 16" aria-label="Fax"><path d="M4 1h6l2 2v3H4zM1 7h14v6h-3v2H4v-2H1zM5 11v3h6v-3z"/></svg>
        <span>555 376 9150</span>
      </div>
      <div class="contact-row">
        <svg viewBox="0 0 16 16" aria-label="Email"><path d="M1 3h14v10H1zM2.5 4.5 8 9l5.5-4.5v7h-11z" fill-rule="evenodd"/></svg>
        <span>info@kestraflowsupply.example</span>
      </div>
      <div class="contact-row">
        <svg viewBox="0 0 16 16" aria-label="Location"><path d="M8 1a5 5 0 0 1 5 5c0 4-5 9-5 9S3 10 3 6a5 5 0 0 1 5-5zm0 3a2 2 0 1 0 0 4 2 2 0 0 0 0-4z" fill-rule="evenodd"/></svg>
        <span class="address">713 Box 2 , Comp 4, RR 3<br>Alder Falls, WR, X9Z 4Q8<br>3-17-52-4W4M<br>Hwy 905 Between RR37 &amp; RR38</span>
      </div>
    </div>

    <div class="back-band"></div>
  </section>

</main>
</body>
</html>
```